KBMR new business card design

We need a business card design for our established business which is Australia wide however based in Melbourne. We are a young team of Financial Planners who specialize in Insurance and Basic super advice for people like us.

We are people who help our clients get things done in a timely and cost effective manner whilst having a good time and a laugh along the way.

We would like this to have a consistent feel with our new e-brochure which i have attached from a color and font perspective.

Industry/Entity Type

Business

Requirements
Must have
• We do not need specific address details rather just the states we are in:

VIC/NSW/QLD/TAS
Nice to have
• Curved edge to mate the brochure

```html
<!DOCTYPE html>
<html lang="en">
<head>
<meta charset="utf-8">
<title>KBMR business card design</title>
<link rel="stylesheet" href="https://fonts.googleapis.com/css2?family=Arimo:ital,wght@0,400;0,700;1,700&family=Source+Sans+3:wght@400&display=swap">
<style>
:root{
  --page:#e9e6e1;
  --label:#1e1e1e;
  --black:#101010;
  --black-soft:#2a2a2a;
  --green:#6fbf52;
  --green-deep:#00a651;
  --white:#ffffff;
  --grey-text:#7a7a7a;
  --grey-dark:#3d3d3d;
  --rule:#b5b5b5;
}
*{box-sizing:border-box;margin:0;padding:0}
html,body{width:1200px;height:788px;overflow:hidden}
body{background:var(--page);position:relative;font-family:"Arimo",Arial,sans-serif}
.view-label{position:absolute;font-family:"Source Sans 3",sans-serif;font-size:22px;color:var(--label);transform:translateX(-50%)}
.card{position:absolute;width:525px;height:300px;border-radius:18px;overflow:hidden}
.card--front{left:53px;top:72px;background:radial-gradient(circle at 45% 45%,var(--black-soft),var(--black) 70%)}
.card--back-one{left:622px;top:74px;background:var(--white)}
.card--back-two{left:53px;top:445px;background:var(--white)}
.card--back-three{left:622px;top:445px;background:radial-gradient(circle at 35% 50%,#2b2b2b,var(--black) 75%)}
.wave{position:absolute;inset:0}
.brand{position:absolute;display:flex;align-items:center;gap:12px;font-weight:700;letter-spacing:1px}
.brand-square{width:22px;height:22px;background:var(--green)}
.brand--front{left:60px;top:100px;font-size:50px;color:var(--white)}
.brand--back-one{left:75px;top:105px;font-size:50px;color:#1a1a1a}
.brand--back-three{left:62px;top:100px;font-size:62px;color:var(--white)}
.states{position:absolute;left:62px;top:268px;font-size:13px;color:var(--white)}
.contact{position:absolute;right:20px;top:92px;text-align:right;color:var(--white)}
.contact-name{font-size:17px;font-weight:700}
.contact-cred,.contact-role{font-size:13.5px;font-weight:700;margin-top:3px}
.contact-lines{margin-top:22px;font-size:13.5px;line-height:24px}
.contact-lines b{font-style:italic;font-weight:700}
.divider{position:absolute;left:260px;top:22px;width:2px;height:232px;background:linear-gradient(transparent,var(--rule) 20%,#555 50%,var(--rule) 80%,transparent)}
.specialties{position:absolute;list-style:none;font-weight:700}
.specialties-title{font-size:18px;font-style:italic;margin-bottom:14px}
.specialties li{font-size:14px;height:34px}
.specialties li::before{content:"\25AA\00a0";}
.specialties--back-one{left:320px;top:47px;color:var(--grey-text)}
.specialties--back-two{left:0;right:0;top:46px;text-align:center;color:var(--grey-dark)}
.specialties--back-three{left:314px;top:26px;color:var(--white)}
.tagline-band{position:absolute;left:0;right:0;bottom:0;height:38px;background:var(--green);color:var(--white);font-size:14px;font-weight:700;display:flex;align-items:center;justify-content:center}
.tagline{position:absolute;font-weight:700;font-size:14px}
.tagline--back-two{left:0;right:0;top:268px;text-align:center;color:var(--grey-dark)}
.tagline--back-three{left:313px;top:254px;color:var(--green);line-height:18px}
</style>
</head>
<body>
<span class="view-label" style="left:320px;top:33px">Front</span>
<span class="view-label" style="left:896px;top:33px">Back - 1</span>
<span class="view-label" style="left:310px;top:404px">Back - 2</span>
<span class="view-label" style="left:896px;top:404px">Back - 3</span>

<section class="card card--front">
  <svg class="wave" viewBox="0 0 525 300" aria-hidden="true">
    <path d="M395 0 C355 70 330 200 250 300 L525 300 L525 0 Z" fill="var(--green-deep)"/>
    <path d="M410 0 C368 70 345 200 268 300 L525 300 L525 0 Z" fill="var(--black)"/>
    <path d="M432 0 C385 80 360 210 290 300 L525 300 L525 0 Z" fill="var(--green)"/>
  </svg>
  <div class="brand brand--front"><span>KBMR</span><span class="brand-square"></span></div>
  <p class="states">VIC/NSW/QLD/TAS</p>
  <div class="contact">
    <p class="contact-name">Daniel Hartley</p>
    <p class="contact-cred">ADFS, BBus, LRS©</p>
    <p class="contact-role">Financial Adviser</p>
    <p class="contact-lines">
      <b>cell</b> 0412 555 018<br>
      <b>phone</b> 1300 555 204<br>
      <b>fax</b> 03 9555 0147<br>
      <b>email</b> daniel@kbmr.com.au<br>
      <b>web</b> www.kbmr.com.au
    </p>
  </div>
</section>

<section class="card card--back-one">
  <div class="brand brand--back-one"><span>KBMR</span><span class="brand-square"></span></div>
  <div class="divider"></div>
  <ul class="specialties specialties--back-one">
    <p class="specialties-title">Specialising in</p>
    <li>Risk Insurance</li><li>Debt Management</li><li>Superannuation</li><li>Wealth Creation</li><li>Retirement Planning</li>
  </ul>
  <p class="tagline-band">SECURE FUTURE, ENHANCED LIFESTYLE</p>
</section>

<section class="card card--back-two">
  <ul class="specialties specialties--back-two">
    <p class="specialties-title">Specialising in</p>
    <li>Risk Insurance</li><li>Debt Management</li><li>Superannuation</li><li>Wealth Creation</li><li>Retirement Planning</li>
  </ul>
  <p class="tagline tagline--back-two">SECURE FUTURE, ENHANCED LIFESTYLE</p>
</section>

<section class="card card--back-three">
  <div class="brand brand--back-three"><span>KBMR</span><span class="brand-square"></span></div>
  <ul class="specialties specialties--back-three">
    <p class="specialties-title">Specialising in</p>
    <li>Risk Insurance</li><li>Debt Management</li><li>Superannuation</li><li>Wealth Creation</li><li>Retirement Planning</li>
  </ul>
  <p class="tagline tagline--back-three">SECURE FUTURE<br>ENHANCED LIFESTYLE</p>
</section>
</body>
</html>
```